Web Site

Target Market(s)

CEOs and International Sales & Marketing Directors of International Companies who wish to expand their business reach to Dubai and the Middle East and are looking for a local professional partner to work with.

Requirements
Must have
• Creativity is key. We don't want the normal standard boxes of text and boxes of pics. Be as creative as you like.
Nice to have
• (This is only a suggestion, we welcome your creativity)
- The center of all pages could be large rotating pictures which display professional corporate men/women working in an office, images of Dubai, the UAE, skyscrapers of business towers in Dubai, ..etc.
- Images should reflect Dubai and the Arab World as a modern, fast-paced, growing modern market - Not Traditional)
Should not have
• Not so colorful, the fewer colors you use, the better.
Not Crammed or Busy
Not Traditional but modern

```html
<!DOCTYPE html>
<html lang="en">
<head>
<meta charset="utf-8">
<title>Kern Group</title>
<link rel="stylesheet" href="https://fonts.googleapis.com/css2?family=Arimo:wght@400;700&family=Varela+Round&family=Yanone+Kaffeesatz:wght@400;500&display=swap">
<style>
:root{
  --bg:#f1f1f1;
  --panel:#f2f2f2;
  --ink:#1c1c1c;
  --red:#8b2119;
  --red-dark:#6e1a13;
  --dark:#2a2a2a;
  --line:#333;
  --white:#fff;
}
*{box-sizing:border-box;margin:0;padding:0}
html,body{width:1023px;height:1200px;overflow:hidden}
body{position:relative;background:var(--bg);font-family:"Arimo",Arial,sans-serif;color:var(--ink)}
.abs{position:absolute}
.brand{left:83px;top:34px;display:flex;align-items:center;gap:10px;font-family:"Arimo",Arial,sans-serif;font-weight:700;font-size:34px;color:var(--dark);letter-spacing:1px}
.brand-mark{width:14px;height:14px;background:var(--red)}
.contact-top{left:763px;top:22px;font-size:13px;line-height:23px}
.contact-top span{display:inline-block;width:46px;color:var(--red);font-family:"Varela Round",sans-serif;font-size:14px}
.contact-top b{font-weight:700;font-size:12.5px}
.nav{left:65px;top:115px;width:891px;height:40px;background:var(--red);display:flex;align-items:center;padding-left:8px}
.nav a{color:var(--white);text-decoration:none;font-size:12.6px;margin-right:18.5px;position:relative;white-space:nowrap}
.nav a.current::after{content:"";position:absolute;left:16px;top:22px;border:5px solid transparent;border-bottom-color:#222}
.rule{left:0;top:154px;width:1023px;height:2px;background:var(--line)}
.slider{left:65px;top:165px;width:892px;height:479px;border:2px solid var(--line);background:var(--panel)}
.slide-photo{position:absolute;left:0;top:0;width:888px;height:382px;background:linear-gradient(180deg,#b9c6d3 0%,#8ea4bb 30%,#6f8296 60%,#c8ccd1 100%);border-bottom:2px solid var(--line)}
.dots{position:absolute;right:26px;top:11px;display:flex;gap:5px}
.dots i{width:10px;height:10px;border-radius:50%;background:#222}
.dots i:first-child{background:#555}
.tab{position:absolute;background:var(--red);color:var(--white);font-family:"Varela Round",sans-serif;padding:0 6px;border-radius:3px 3px 0 0}
.tab-welcome{left:16px;top:346px;height:36px;width:112px;font-size:21px;line-height:40px}
.intro{position:absolute;left:18px;top:392px;width:800px;font-size:13.5px;line-height:18.6px}
.intro strong{font-weight:700}
.btn-more{position:absolute;left:808px;top:409px;width:56px;height:29px;background:var(--red);color:var(--white);font-family:"Yanone Kaffeesatz",sans-serif;font-weight:500;font-size:19px;text-align:center;line-height:29px;border-radius:2px}
.tab-what{left:83px;top:663px;height:34px;width:113px;font-size:17.5px;line-height:40px}
.divisions{left:65px;top:696px;width:893px;height:49px;background:var(--dark);display:flex;overflow:hidden}
.divisions a{flex:none;color:var(--white);text-decoration:none;font-family:"Yanone Kaffeesatz",sans-serif;font-size:18.5px;line-height:49px;text-align:center;border-right:1px solid #555;white-space:nowrap}
.divisions a:last-child{border-right:0}
.divisions a.active span{border-bottom:2px solid var(--white);padding-bottom:3px}
.division-panel{left:65px;top:745px;width:893px;height:178px;border:2px solid var(--line);border-top:0;background:var(--panel)}
.division-photo{position:absolute;left:22px;top:17px;width:224px;height:105px;border:2px solid #333;background:linear-gradient(120deg,#e8e8e8 0%,#bdbdbd 45%,#5a3a2e 70%,#2b1a14 100%)}
.division-title{position:absolute;left:256px;top:14px;font-family:"Yanone Kaffeesatz",sans-serif;font-weight:500;font-size:21px}
.division-text{position:absolute;left:257px;top:43px;width:615px;font-size:13.5px;line-height:18.6px}
.btn-read{position:absolute;left:778px;top:124px;width:87px;height:27px;background:var(--dark);color:var(--white);border-radius:10px;font-size:13.5px;font-weight:700;text-align:center;line-height:27px}
.footer{left:0;top:952px;width:1023px;height:248px;background:linear-gradient(180deg,var(--red-dark),#8a2a20)}
.footer h3{position:absolute;font-family:"Varela Round",sans-serif;font-weight:400;font-size:14.5px;color:#eee}
.footer ul{position:absolute;list-style:none;font-size:13px;line-height:22.4px;color:var(--white)}
.field{position:absolute;left:750px;width:179px;height:21px;border:1px solid #eee;color:var(--white);font-weight:700;font-size:13px;padding-left:3px;line-height:18px}
.btn-send{position:absolute;left:821px;top:210px;width:65px;height:23px;background:#f2f2f2;color:var(--dark);border-radius:4px;font-family:"Yanone Kaffeesatz",sans-serif;font-weight:500;font-size:18px;text-align:center;line-height:24px}
.copyright{position:absolute;left:69px;top:226px;font-size:11.5px;color:var(--white)}
</style>
</head>
<body>
<div class="abs brand"><span class="brand-mark"></span>KERN GROUP</div>
<div class="abs contact-top">
  <div><span>Call</span><b>+971 4 555 0142</b></div>
  <div><span>Email</span><b>info@kerngroup.example</b></div>
</div>

<nav class="abs nav">
  <a class="current">HOME</a><a>ABOUT THE GROUP</a><a>CHAIRMAN’S MESSAGE</a><a>DIVISIONS</a><a>GROUP COMPANIES</a><a>EMPLOYMENT &amp; ASSOCIATION</a><a>CONTACT US</a>
</nav>
<div class="abs rule"></div>

<section class="abs slider">
  <div class="slide-photo" role="img" aria-label="City skyline of modern business towers"></div>
  <div class="dots"><i></i><i></i><i></i></div>
  <div class="tab tab-welcome">Welcome</div>
  <p class="intro"><strong>KERN group</strong> is a <strong>Dubai-based</strong> diversified groups of companies led by its chairman <strong>Mr. Rashid Hamdan Al Noor</strong>, a member of a <strong>long-established family of Dubai</strong>. The Group has grown with Dubai, and while best known for Real Estate Investment, it is globally recognized through its involvement in the Legal Consultations, Media Production, General Trading, and Telecommunication Services sectors.</p>
  <div class="btn-more">MORE</div>
</section>

<div class="abs tab tab-what">What we do</div>
<nav class="abs divisions">
  <a class="active" style="width:141px"><span>Legal Consultation</span></a><a style="width:125px">Tamra’s Studios</a><a style="width:196px">Kern Real Estate Investment</a><a style="width:153px">Kern General Trading</a><a style="width:163px">Kern Business Services</a><a style="width:115px">Kern Telecom</a>
</nav>
<section class="abs division-panel">
  <div class="division-photo" role="img" aria-label="Judge's gavel on a desk"></div>
  <h2 class="division-title">Legal Consultation</h2>
  <p class="division-text">Lorem ipsum dolor sit amet, cu iracundia pertinacia pri. Cu sea causae utamur sensibus, id sint iusto regione cum. His ei epicuri noluisse appellantur, nec eruditi petentium expetenda ex. Ea graeci deleniti concludaturque nam. Sed veniam doctus suscipit te. Et nihil appareat recteque mei, meis option id pri. Pri in sumo enim invenire.</p>
  <div class="btn-read">Read more</div>
</section>

<footer class="abs footer">
  <h3 style="left:79px;top:16px">The Company</h3>
  <ul style="left:80px;top:43px"><li>About the Group</li><li>Chairman’s Message</li><li>Divisions</li><li>Employment &amp; Association</li></ul>
  <h3 style="left:293px;top:16px">Group Companies</h3>
  <ul style="left:293px;top:42px"><li>Legal Consultation</li><li>Tamra’s Studio</li><li>Kern Real Estate Investment</li><li>Kern General Trading</li><li>Kern Business Servcies</li><li>Kern Telecome</li></ul>
  <h3 style="left:509px;top:18px">Other Links</h3>
  <ul style="left:516px;top:42px"><li>Sitemap</li><li>Privacy Policy</li><li>Terms of Use</li><li>Contact Us</li></ul>
  <h3 style="left:744px;top:19px">Contact us</h3>
  <div class="field" style="top:45px">Name</div>
  <div class="field" style="top:77px">Email</div>
  <div class="field" style="top:110px">Mobile</div>
  <div class="field" style="top:146px;height:53px">Enquiry</div>
  <div class="btn-send">SEND</div>
  <p class="copyright">Copyright 2012 Kern Group. All rights reserved.</p>
</footer>
</body>
</html>
```